Tolland Imaging
Mobile Ultrasound Solutions
Professional
Helen Marsh
Executive Sales Representative
San Antonio, Texas
info@tollandimaging-example.com
tollandimaging-example.com

```html
<!DOCTYPE html>
<html lang="en">
<head>
<meta charset="utf-8">
<title>Tolland Imaging Stationery</title>
<link href="https://fonts.googleapis.com/css2?family=Open+Sans:wght@400;600;700&display=swap" rel="stylesheet">
<style>
:root{
  --bg-light:#6c6c6c;
  --bg-dark:#2c2c2c;
  --paper:#ffffff;
  --brand:#2d63b7;
  --brand-deep:#1b3f8e;
  --brand-soft:#dfe8f5;
  --ink:#4a4a4a;
}
*{margin:0;padding:0;box-sizing:border-box}
html,body{width:1200px;height:346px;overflow:hidden}
body{
  position:relative;
  font-family:"Open Sans",Arial,sans-serif;
  background:radial-gradient(ellipse at 50% 20%,var(--bg-light) 0%,#4a4a4a 55%,var(--bg-dark) 100%);
}
.item{position:absolute;background:var(--paper);box-shadow:0 2px 6px rgba(0,0,0,.45)}
.brand{display:flex;align-items:center;gap:4px;color:var(--brand);font-weight:700;white-space:nowrap}
.brand .dot{border-radius:50%;background:var(--brand);flex:none}
.small{color:var(--ink);font-size:4px;line-height:6px;white-space:nowrap}

/* business card */
.card{left:19px;top:125px;width:137px;height:86px}
.card .brand{position:absolute;left:9px;top:10px;font-size:6px}
.card .brand .dot{width:9px;height:9px}
.card .person{position:absolute;left:58px;top:38px}
.card .person .name{color:var(--brand);font-size:5.5px;font-weight:700;line-height:7px}
.card .band{position:absolute;left:0;right:0;bottom:0;height:7px;background:linear-gradient(90deg,var(--brand),var(--brand-deep))}

/* letterhead */
.letterhead{top:22px;width:226px;height:285px}
.letterhead.one{left:163px}
.letterhead.two{left:398px}
.letterhead .brand{position:absolute;left:18px;top:18px;font-size:7px}
.letterhead .brand .dot{width:12px;height:12px}
.letterhead .contact{position:absolute;left:150px;top:16px}
.letterhead .faint-mark{position:absolute;left:73px;top:112px;width:82px;height:82px;border-radius:50%;background:var(--brand-soft);opacity:.8}
.letterhead .band{position:absolute;left:0;right:0;bottom:12px;height:3px;background:var(--brand)}
.letterhead .footer{position:absolute;left:0;right:0;bottom:4px;text-align:center;font-size:3.5px;color:var(--ink);white-space:nowrap}

/* envelope */
.envelope{left:636px;width:228px;height:101px}
.envelope.upper{top:98px}
.envelope.lower{top:218px}
.envelope .brand{position:absolute;left:10px;top:9px;font-size:6px}
.envelope .brand .dot{width:9px;height:9px}
.envelope .faint-mark{position:absolute;left:94px;top:20px;width:40px;height:40px;border-radius:50%;background:var(--brand-soft);opacity:.7}
.envelope .band{position:absolute;left:0;right:0;bottom:10px;height:4px;background:linear-gradient(90deg,var(--brand-deep),var(--brand))}
.envelope .footer{position:absolute;left:0;right:0;bottom:2px;text-align:center;font-size:3.5px;color:var(--ink)}

/* logo display */
.logo-display{position:absolute;left:912px;top:20px;width:216px;height:90px;display:flex;flex-direction:column;align-items:center;justify-content:center;gap:6px}
.logo-display .brand{font-size:17px;color:#3a73c9;gap:8px}
.logo-display .brand .dot{width:26px;height:26px;background:#3a73c9}
.logo-display .tagline{color:#c9d3e2;font-size:6px;letter-spacing:.5px}

/* envelope back with flap */
.envelope-back{left:907px;top:132px;width:288px;height:108px}
.envelope-back svg{display:block}
.envelope-back .brand{position:absolute;left:120px;top:18px;font-size:4px;color:#ffffff}
.envelope-back .brand .dot{width:6px;height:6px;background:#ffffff}

/* envelope front */
.envelope-front{left:898px;top:204px;width:250px;height:110px;box-shadow:0 3px 8px rgba(0,0,0,.5)}
.envelope-front svg{position:absolute;left:0;top:0}
.envelope-front .brand{position:absolute;left:112px;top:42px;font-size:4px}
.envelope-front .brand .dot{width:6px;height:6px}
</style>
</head>
<body>

<section class="item card" aria-label="Business card">
  <div class="brand"><span class="dot"></span>Tolland Imaging</div>
  <div class="person">
    <p class="name">Helen Marsh</p>
    <p class="small">Executive Sales Representative</p>
    <p class="small">San Antonio, Texas</p>
    <p class="small">info@tollandimaging-example.com</p>
    <p class="small">tollandimaging-example.com</p>
  </div>
  <div class="band"></div>
</section>

<section class="item letterhead one" aria-label="Letterhead">
  <div class="brand"><span class="dot"></span>Tolland Imaging</div>
  <div class="contact small">
    <p>Helen Marsh</p>
    <p>San Antonio, Texas</p>
    <p>info@tollandimaging-example.com</p>
    <p>tollandimaging-example.com</p>
  </div>
  <div class="faint-mark"></div>
  <div class="band"></div>
  <p class="footer">tollandimaging-example.com · info@tollandimaging-example.com · San Antonio, Texas</p>
</section>

<section class="item letterhead two" aria-label="Continuation letterhead">
  <div class="brand"><span class="dot"></span>Tolland Imaging</div>
  <div class="faint-mark"></div>
  <div class="band"></div>
  <p class="footer">tollandimaging-example.com · info@tollandimaging-example.com · San Antonio, Texas</p>
</section>

<section class="item envelope upper" aria-label="Envelope">
  <div class="brand"><span class="dot"></span>Tolland Imaging</div>
  <div class="faint-mark"></div>
  <div class="band"></div>
  <p class="footer">tollandimaging-example.com</p>
</section>

<section class="item envelope lower" aria-label="Envelope">
  <div class="brand"><span class="dot"></span>Tolland Imaging</div>
  <div class="faint-mark"></div>
  <div class="band"></div>
  <p class="footer">tollandimaging-example.com</p>
</section>

<section class="logo-display" aria-label="Logo">
  <div class="brand"><span class="dot"></span>Tolland Imaging</div>
  <p class="tagline">Mobile Ultrasound Solutions</p>
</section>

<section class="item envelope-back" aria-label="Envelope back">
  <svg width="288" height="108" viewBox="0 0 288 108">
    <defs>
      <linearGradient id="flap-fill" x1="0" y1="0" x2="0" y2="1">
        <stop offset="0" stop-color="#1b3f8e"/>
        <stop offset="1" stop-color="#3f74c8"/>
      </linearGradient>
    </defs>
    <rect width="288" height="108" fill="#ffffff"/>
    <polygon points="0,0 288,0 288,18 144,56 0,18" fill="url(#flap-fill)"/>
    <polyline points="0,24 144,62 288,24" fill="none" stroke="#c9d6ea" stroke-width="1"/>
  </svg>
  <div class="brand"><span class="dot"></span>Tolland Imaging</div>
</section>

<section class="item envelope-front" aria-label="Envelope front">
  <svg width="250" height="110" viewBox="0 0 250 110">
    <polyline points="0,0 125,58 250,0" fill="none" stroke="#e3e7ee" stroke-width=".8"/>
    <line x1="0" y1="110" x2="105" y2="66" stroke="#e3e7ee" stroke-width=".8"/>
    <line x1="250" y1="110" x2="145" y2="66" stroke="#e3e7ee" stroke-width=".8"/>
  </svg>
  <div class="brand"><span class="dot"></span>Tolland Imaging</div>
</section>

</body>
</html>
```